Meridane Works, Inc. - Update our Website

Meridane Works needs a website to help our customers to navigate through our services efficiently. Our existing website is at www.meridwork.example

We would like to explain our services with content and pictures (photographs) that distinguishes our products and services from our competition.

The website design must implement a strategy to focus on our Contract Labeling services.

With this new design we would like to attract new customers and ensure that our existing customers are fully informed with our latest offerings.

```html
<!DOCTYPE html>
<html lang="en">
<head>
<meta charset="utf-8">
<title>Meridane Works, Inc.</title>
<link href="https://fonts.googleapis.com/css2?family=Raleway:wght@300;400;600;700&display=swap" rel="stylesheet">
<style>
:root{
  --accent:#29b0f0;
  --ink:#1b1f24;
  --muted:#8a8f96;
  --band:#f3f3f3;
  --footer:#131d2a;
  --footer-deep:#0e1620;
  --footer-text:#6d7784;
  --white:#ffffff;
}
*{margin:0;padding:0;box-sizing:border-box}
html,body{width:1046px;height:1200px;overflow:hidden}
body{position:relative;background:var(--white);font-family:'Raleway',sans-serif;color:var(--ink)}
.header{position:absolute;left:0;top:0;width:1046px;height:68px;background:var(--white)}
.brand{position:absolute;left:67px;top:20px;display:flex;align-items:center;gap:8px}
.brand-dot{width:26px;height:26px;border-radius:50%;background:var(--accent)}
.brand-name{font-weight:700;font-size:15px;letter-spacing:.5px;color:var(--ink);text-transform:uppercase}
.nav{position:absolute;left:538px;top:0;display:flex;height:68px}
.nav a{display:block;height:68px;line-height:66px;padding:0 16px;font-size:13.5px;color:var(--ink);text-decoration:none}
.nav a.active{background:var(--accent);color:var(--white);position:relative}
.nav a.active::after{content:"";position:absolute;left:50%;bottom:0;margin-left:-5px;border:5px solid transparent;border-bottom-color:var(--white)}
.hero{position:absolute;left:0;top:68px;width:1046px;height:429px;overflow:hidden;
  background:linear-gradient(135deg,#3bb394 0%,#28afc0 30%,#1aa8dc 50%,#3a8fb4 72%,#5d5c44 100%)}
.hero-title{position:absolute;left:0;width:100%;top:100px;text-align:center;font-weight:300;font-size:58px;color:var(--white);letter-spacing:1px}
.hero-sub{position:absolute;left:0;width:100%;top:180px;text-align:center;font-weight:300;font-size:15px;color:#e8f5ee}
.btn-outline{position:absolute;left:473px;top:232px;width:99px;height:36px;border:1px solid var(--white);color:var(--white);font-size:12px;font-weight:600;text-align:center;line-height:34px}
.dots{position:absolute;left:483px;top:406px;display:flex;gap:5px}
.dots span{width:23px;height:3px;background:rgba(255,255,255,.5)}
.dots span.on{background:#111}
.welcome-title{position:absolute;left:0;width:100%;top:555px;text-align:center;font-weight:300;font-size:31px;text-transform:uppercase}
.welcome-sub{position:absolute;left:0;width:100%;top:592px;text-align:center;font-weight:300;font-size:17.5px;color:var(--accent);text-transform:uppercase}
.feature{position:absolute;top:656px;width:300px}
.feature-icon{position:absolute;left:0;top:0;width:53px;height:53px;border:1px solid #e2e2e2;border-radius:50%;display:flex;align-items:center;justify-content:center}
.feature-body{position:absolute;left:78px;top:0;width:215px}
.feature h3{font-size:14.5px;font-weight:600;text-transform:uppercase;line-height:16px}
.feature p{margin-top:6px;font-size:12px;font-weight:300;line-height:21.7px;color:var(--muted)}
.cta-band{position:absolute;left:0;top:831px;width:1046px;height:112px;background:var(--band)}
.cta-title{position:absolute;left:145px;top:30px;font-weight:300;font-size:30px;text-transform:uppercase;line-height:32px}
.cta-sub{position:absolute;left:145px;top:63px;font-weight:300;font-size:16.5px;color:var(--accent);text-transform:uppercase}
.btn-solid{position:absolute;left:801px;top:42px;width:98px;height:35px;background:var(--white);font-size:12px;font-weight:600;text-align:center;line-height:35px}
.footer{position:absolute;left:0;top:943px;width:1046px;height:204px;background:var(--footer)}
.footer-tab{position:absolute;left:494px;top:0;width:57px;height:3px;background:var(--accent)}
.footer-brand{position:absolute;left:78px;top:90px;display:flex;align-items:center;gap:8px}
.footer-brand .dot{width:20px;height:20px;border-radius:50%;background:var(--accent)}
.footer-brand span{font-size:15px;font-weight:700;color:var(--white);text-transform:uppercase}
.footer-col{position:absolute;top:37px}
.footer-col h4{font-size:14px;font-weight:700;color:var(--white);text-transform:uppercase;margin-bottom:12px}
.footer-col p,.footer-col li{font-size:11.5px;font-weight:300;color:var(--footer-text);line-height:21.7px}
.footer-col ul{list-style:none}
.footer-col li::before{content:"";display:inline-block;width:4px;height:4px;border-radius:50%;background:var(--footer-text);margin:0 7px 2px 3px}
.contact-line{display:flex;align-items:center;gap:12px;height:24px}
.contact-line svg{width:16px;height:16px}
.bottom-bar{position:absolute;left:0;top:1147px;width:1046px;height:53px;background:var(--footer-deep)}
.bottom-bar p{position:absolute;left:67px;top:19px;font-size:11px;font-weight:300;color:#46505c}
</style>
</head>
<body>
<header class="header">
  <div class="brand"><span class="brand-dot"></span><span class="brand-name">Meridane Works Inc.</span></div>
  <nav class="nav">
    <a class="active" href="#">Home</a>
    <a href="#">About us</a>
    <a href="#">User Support</a>
    <a href="#">Validation</a>
    <a href="#">Contact Us</a>
  </nav>
</header>

<section class="hero" role="img" aria-label="Slide backdrop photograph in soft green, blue and olive tones">
  <h1 class="hero-title">MERIDANE WORKS, INC</h1>
  <p class="hero-sub">Specializes in providing products and services to the pharmaceutical industry.</p>
  <div class="btn-outline">Contact Us</div>
  <div class="dots"><span></span><span class="on"></span><span></span></div>
</section>

<h2 class="welcome-title">Welcome to Meridane Works, Inc..</h2>
<p class="welcome-sub">We are focused on the needs of those individuals involved with clinical trial materials</p>

<div class="feature" style="left:67px">
  <div class="feature-icon"><svg width="24" height="18" viewBox="0 0 24 18"><circle cx="7" cy="5" r="3.2" fill="#29b0f0"/><circle cx="17" cy="5" r="3.2" fill="#29b0f0"/><circle cx="12" cy="6" r="3.6" fill="#29b0f0"/><path d="M1 17c0-5 3-7 6-7s4 1 5 2c1-1 2-2 5-2s6 2 6 7z" fill="#29b0f0"/></svg></div>
  <div class="feature-body"><h3>About us</h3><p>For over two decades we have supported study teams with careful contract labeling of clinical trial materials, from small runs to global programs.</p></div>
</div>
<div class="feature" style="left:378px">
  <div class="feature-icon"><svg width="14" height="20" viewBox="0 0 14 20"><path d="M5 1h4v6l5 12H0L5 7z" fill="#29b0f0"/><circle cx="8" cy="2" r="1" fill="#fff"/></svg></div>
  <div class="feature-body"><h3>Service</h3><p>Our contract labeling service covers label design, multilingual text, printing, blinding and application, all under tight quality control and audit.</p></div>
</div>
<div class="feature" style="left:689px">
  <div class="feature-icon"><svg width="20" height="16" viewBox="0 0 20 16"><path d="M1 5c0-3 18-3 18 0v2h-5V5H6v2H1z" fill="#29b0f0"/><rect x="3" y="8" width="14" height="7" rx="1" fill="#29b0f0"/><circle cx="10" cy="11.5" r="2" fill="#fff"/></svg></div>
  <div class="feature-body"><h3>Contact us</h3><p>Planning a new study? Talk to our labeling team about timelines, label formats and volumes, and get a clear quote for your next trial.</p></div>
</div>

<section class="cta-band">
  <h2 class="cta-title">Meridane Works, Inc</h2>
  <p class="cta-sub">Providing products and services to the pharmaceutical industry.</p>
  <div class="btn-solid">Contact Us</div>
</section>

<footer class="footer">
  <div class="footer-tab"></div>
  <div class="footer-brand"><span class="dot"></span><span>Meridane Works</span></div>
  <div class="footer-col" style="left:300px"><h4>Meridane Works, Inc.</h4><p>Loading...</p></div>
  <div class="footer-col" style="left:533px"><h4>Site</h4>
    <ul><li>Home</li><li>About Us</li><li>User Support</li><li>Validation</li></ul>
  </div>
  <div class="footer-col" style="left:767px"><h4>Contact</h4>
    <div class="contact-line"><svg viewBox="0 0 16 16"><path d="M8 1a4.5 4.5 0 0 0-4.5 4.5C3.5 9 8 15 8 15s4.5-6 4.5-9.5A4.5 4.5 0 0 0 8 1z" fill="#29b0f0"/><circle cx="8" cy="5.5" r="1.7" fill="#131d2a"/></svg><p>52 Alder Lane, Springfield</p></div>
    <div class="contact-line"><svg viewBox="0 0 16 16"><path d="M1 5c0-3 14-3 14 0v2h-4V5H5v2H1z" fill="#29b0f0"/><rect x="3" y="8" width="10" height="6" rx="1" fill="#29b0f0"/></svg><p>+1.555.014.2290</p></div>
    <div class="contact-line"><svg viewBox="0 0 16 16"><rect x="1" y="3" width="14" height="10" fill="#29b0f0"/><path d="M1 3l7 6 7-6" fill="none" stroke="#131d2a" stroke-width="1.3"/></svg><p>hello@meridwork.example</p></div>
  </div>
</footer>
<div class="bottom-bar"><p>Meridane Works, Inc. All rights reserved.</p></div>
</body>
</html>
```